Real Estate Business card design

Company Name: Thornbury Holdings, LLC
subtitle: We pay cash for houses!
Martin Calloway
Managing Director
518-674-2913
Mart@ThornburyHoldingsLLC.example
www.ThornburyHoldingsLLC.example

We pay referral fees for Seller and Buyer leads.

Back:
We offer referral fees for Seller and Buyer leads that close.

Please contact Ned at 518-674-2913 with your referrals or to learn more about the referral program!

I am open to different color options but I am going for a classic, elegant, clean, and professional look. Please use logo as a reference.

Target Market(s)

People selling their homes and people in the market for buying homes.

Contact Information for Business Card

please see project description

Font styles to use
Serif
Sans Serif
Script

Requirements
Must have
• must have my logo in it
Nice to have
• I like cards that are split down the middle but please come up with a few mock ups. Open to any color scheme.

```html
<!DOCTYPE html>
<html lang="en">
<head>
<meta charset="utf-8">
<title>Thornbury Holdings, LLC – Business Cards</title>
<link rel="stylesheet" href="https://fonts.googleapis.com/css2?family=Fira+Sans:wght@400;500;600&family=Roboto:wght@400;500&family=Roboto+Condensed:wght@400&display=swap">
<style>
  :root {
    --backdrop: #2e2f31;
    --paper-light: #f1f1f0;
    --paper-shade: #dcdcdb;
    --slate: #3b4350;
    --slate-deep: #363d49;
    --gold: #c39a77;
    --gold-light: #d6b596;
    --gold-dark: #a77d5b;
    --ink: #1e1e1e;
  }
  * { margin: 0; padding: 0; box-sizing: border-box; }
  html, body { width: 1200px; height: 1138px; overflow: hidden; }
  body {
    background: var(--backdrop);
    position: relative;
    font-family: "Roboto", sans-serif;
    color: var(--ink);
  }
  .card {
    position: absolute;
    border-radius: 18px;
    overflow: hidden;
    background: linear-gradient(180deg, var(--paper-light) 0%, #ececeb 70%, var(--paper-shade) 100%);
    box-shadow: 0 6px 14px rgba(0,0,0,0.45);
  }

  /* Referral side */
  .card--referral { left: 274px; top: 186px; width: 623px; height: 376px; }
  .brand-mark {
    position: absolute; left: 0; right: 0; top: 54px;
    display: flex; flex-direction: column; align-items: center;
  }
  .brand-mark__square {
    width: 26px; height: 26px; background: var(--gold);
    margin-bottom: 18px;
  }
  .brand-mark__name {
    font-family: "Fira Sans", sans-serif; font-weight: 500;
    color: var(--slate); text-align: center; line-height: 1;
  }
  .brand-mark__name .line-main { display: block; font-size: 62px; letter-spacing: 0.5px; }
  .brand-mark__name .line-sub { display: block; font-size: 27px; letter-spacing: 1.5px; margin-top: 6px; }

  .referral-band {
    position: absolute; left: 0; right: 0; top: 245px; height: 88px;
    background: linear-gradient(90deg, var(--gold-dark), var(--gold-light) 50%, var(--gold-dark));
    text-align: center; color: var(--ink);
    display: flex; flex-direction: column; justify-content: center;
  }
  .referral-band p { font-size: 17px; line-height: 23px; white-space: nowrap; }
  .referral-band .referral-band__call {
    font-family: "Fira Sans", sans-serif; font-weight: 600; font-size: 20px;
  }
  .site-line {
    position: absolute; left: 0; right: 0; top: 336px;
    display: flex; align-items: center; justify-content: center; gap: 20px;
    font-size: 17px;
  }
  .site-line__rule {
    width: 68px; height: 2px;
    background: linear-gradient(90deg, transparent, var(--gold-dark), transparent);
  }

  /* Contact side */
  .card--contact { left: 276px; top: 608px; width: 618px; height: 374px; }
  .contact-panel { position: absolute; left: 0; top: 0; }
  .panel-brand {
    position: absolute; left: 0; width: 266px; top: 140px; text-align: center;
    font-family: "Fira Sans", sans-serif; font-weight: 500; color: #ffffff; line-height: 1;
  }
  .panel-brand__square { width: 18px; height: 18px; background: var(--gold); margin: 0 auto 10px; }
  .panel-brand .line-main { display: block; font-size: 38px; }
  .panel-brand .line-sub { display: block; font-size: 18px; letter-spacing: 1.2px; margin-top: 4px; }
  .panel-tagline {
    position: absolute; left: 0; width: 266px; top: 252px; text-align: center;
    font-family: "Roboto", sans-serif; font-weight: 500; font-size: 14px; color: var(--gold);
    white-space: nowrap;
  }
  .person {
    position: absolute; right: 24px; top: 38px; text-align: right;
  }
  .person__name {
    font-family: "Fira Sans", sans-serif; font-weight: 500; font-size: 31px; color: var(--slate);
  }
  .person__title { font-size: 18px; margin-top: 4px; }
  .gold-dot {
    position: absolute; right: -14px; top: 48px; width: 34px; height: 40px;
    border-radius: 50%; background: var(--gold);
  }
  .contact-list {
    position: absolute; right: 24px; top: 224px; list-style: none; text-align: right;
  }
  .contact-list li {
    display: flex; align-items: center; justify-content: flex-end; gap: 7px;
    font-size: 18px; height: 25.5px; white-space: nowrap;
  }
  .contact-list svg { width: 15px; height: 15px; flex: none; }
  .referral-strip {
    position: absolute; left: 244px; right: 22px; top: 312px; height: 36px;
    background: linear-gradient(90deg, var(--gold-dark), var(--gold-light) 60%, var(--gold));
    font-family: "Roboto Condensed", sans-serif; font-size: 17px; white-space: nowrap;
    display: flex; align-items: center; justify-content: flex-end; padding-right: 4px;
  }
</style>
</head>
<body>

<section class="card card--referral" aria-label="Referral side of business card">
  <div class="brand-mark">
    <div class="brand-mark__square"></div>
    <div class="brand-mark__name">
      <span class="line-main">Thornbury</span>
      <span class="line-sub">Holdings, LLC</span>
    </div>
  </div>
  <div class="referral-band">
    <p>We offer referral fees for Seller and Buyer leads that close.</p>
    <p class="referral-band__call">Please Contact Ned at 518-674-2913</p>
    <p>with your referrals or to learn more about the referral program!</p>
  </div>
  <div class="site-line">
    <span class="site-line__rule"></span>
    <span>www.ThornburyHoldingsLLC.example</span>
    <span class="site-line__rule"></span>
  </div>
</section>

<section class="card card--contact" aria-label="Contact side of business card">
  <svg class="contact-panel" width="618" height="374" viewBox="0 0 618 374" aria-hidden="true">
    <defs>
      <linearGradient id="edge-gold" x1="0" y1="0" x2="0" y2="1">
        <stop offset="0" stop-color="#d6b596"/>
        <stop offset="0.6" stop-color="#c39a77"/>
        <stop offset="1" stop-color="#a77d5b"/>
      </linearGradient>
    </defs>
    <path d="M0 0 H222 C262 80 268 240 208 374 H0 Z" fill="url(#edge-gold)"/>
    <path d="M0 0 H214 C254 80 258 240 198 374 H0 Z" fill="#3b4350"/>
  </svg>
  <div class="panel-brand">
    <div class="panel-brand__square"></div>
    <span class="line-main">Thornbury</span>
    <span class="line-sub">Holdings, LLC</span>
  </div>
  <p class="panel-tagline">WE PAY CASH FOR HOUSES!</p>

  <div class="gold-dot"></div>
  <div class="person">
    <h1 class="person__name">Martin Calloway</h1>
    <p class="person__title">Managing Director</p>
  </div>

  <ul class="contact-list">
    <li>518-674-2913
      <svg viewBox="0 0 16 16"><path d="M2 6c0-3 3-4 6-4s6 1 6 4l-3 1-1-2H6L5 7z M4 8h8l1 6H3z" fill="#c39a77"/></svg>
    </li>
    <li>Mart@ThornburyHoldingsLLC.example
      <svg viewBox="0 0 16 16"><rect x="1" y="3" width="14" height="10" fill="#c39a77"/><path d="M1 3l7 6 7-6" fill="none" stroke="#f1f1f0" stroke-width="1.2"/></svg>
    </li>
    <li>www.ThornburyHoldingsLLC.example
      <svg viewBox="0 0 16 16"><circle cx="8" cy="8" r="6.5" fill="none" stroke="#c39a77" stroke-width="1.4"/><path d="M1.5 8h13M8 1.5c-3 3-3 10 0 13M8 1.5c3 3 3 10 0 13" fill="none" stroke="#c39a77" stroke-width="1.1"/></svg>
    </li>
  </ul>

  <div class="referral-strip">We Pay Referral Fees For Seller &amp; Buyer Leads!</div>
</section>

</body>
</html>
```